Real Estate Sign

My company is in need of a redesign for our real estate lawn sign. The sign should show our logo, the phrase "For Sale", our phone number 314-587-2049 and website www.HomvexTX.com.
Updates

Hello

Thank you for your submissions.  I am looking for the website and phone number to be very visible from a good distance.  I do also want to stay within the colors of my logo. Too many colors could be expensive to reproduce.

Thank you
Trevor

I favor clean, straight lines and design.  I prefer not to add any other graphics or logos on the sign.  The logo and name are enough. I am looking for readability from a good distance and prefer calls to action like call 314-592-2049 for information or visit www.HomvexTX.com to schedule tour today!  I don't really need FOR SALE to be so prominent.

thanks for all the submissions.
Trevor

Trevor

Industry/Entity Type

Real Estate

```html
<!DOCTYPE html>
<html lang="en">
<head>
<meta charset="utf-8">
<title>Homvex TX – For Sale Lawn Sign</title>
<link rel="stylesheet" href="https://fonts.googleapis.com/css2?family=Arimo:wght@700&family=PT+Sans:wght@700&display=swap">
<style>
  :root {
    --navy: #0d3f6e;
    --sky: #29a7df;
    --white: #ffffff;
    --backdrop: #f3f4f6;
  }
  * { margin: 0; padding: 0; box-sizing: border-box; }
  html, body {
    width: 1200px;
    height: 1020px;
    overflow: hidden;
    background: var(--backdrop);
    font-family: "PT Sans", Arial, sans-serif;
  }
  .sign {
    position: absolute;
    left: 30px;
    top: 130px;
    width: 1140px;
    height: 760px;
    background: var(--white);
    box-shadow: 0 2px 10px rgba(0,0,0,0.12);
  }
  .sign__banner {
    height: 172px;
    background: var(--navy);
    display: flex;
    align-items: center;
    justify-content: center;
  }
  .sign__headline {
    color: var(--white);
    font-family: "Arimo", Arial, sans-serif;
    font-weight: 700;
    font-size: 80px;
    line-height: 1;
  }
  .contact-box {
    position: absolute;
    left: 63px;
    top: 245px;
    width: 1037px;
    height: 176px;
    border: 5px solid var(--navy);
    border-radius: 26px;
    display: flex;
    align-items: center;
  }
  .contact-box__label {
    position: absolute;
    right: 14px;
    top: -50px;
    background: var(--white);
    padding: 0 8px;
    color: var(--sky);
    font-weight: 700;
    font-size: 72px;
    line-height: 1;
    white-space: nowrap;
  }
  .contact-box__icon {
    width: 94px;
    height: 94px;
    margin-left: 16px;
    flex: none;
  }
  .contact-box__phone {
    margin-left: 30px;
    color: var(--navy);
    font-weight: 700;
    font-size: 140px;
    line-height: 1;
    white-space: nowrap;
  }
  .sign__visit,
  .sign__website,
  .sign__cta {
    position: absolute;
    left: 0;
    right: 0;
    text-align: center;
    font-weight: 700;
    line-height: 1;
    white-space: nowrap;
  }
  .sign__visit {
    top: 428px;
    color: var(--sky);
    font-size: 80px;
  }
  .sign__website {
    top: 516px;
    color: var(--navy);
    font-size: 84px;
  }
  .sign__cta {
    top: 608px;
    color: var(--sky);
    font-size: 84px;
  }
</style>
</head>
<body>
  <div class="sign">
    <div class="sign__banner">
      <h1 class="sign__headline">FOR SALE</h1>
    </div>

    <div class="contact-box">
      <span class="contact-box__label">Contact us</span>
      <svg class="contact-box__icon" viewBox="0 0 100 100" aria-hidden="true">
        <circle cx="50" cy="50" r="44" fill="none" stroke="var(--navy)" stroke-width="5"/>
        <path d="M36 24 c-6 3 -10 9 -9 17 c2 16 16 32 32 36 c8 2 14 -1 18 -7 l-10 -9 c-2 -2 -5 -2 -7 0 l-4 4 c-8 -4 -14 -11 -18 -19 l4 -4 c2 -2 2 -5 0 -7 z"
              fill="none" stroke="var(--navy)" stroke-width="5" stroke-linejoin="round"/>
      </svg>
      <span class="contact-box__phone">314-587-2049</span>
    </div>

    <p class="sign__visit">visit</p>
    <p class="sign__website">www.HomvexTX.com</p>
    <p class="sign__cta">TO SCHEDULE TOUR TODAY!</p>
  </div>
</body>
</html>
```